Website for Youth Orchestra to sell tickets and attract young musicians

We are looking for a new website design for a Youth Orchestra; one of the best classical youth orchestras in the county. This project is the design only. <br/><br/>The website serves two main purposes:<br/>• Selling tickets for concerts and performances of the orchestra<br/>• Recruiting young musicians to do audition for the orchestra<br/>
Updates

Target Market(s)

Classical music lovers with a special interest in young upcoming musicians.
Young talented musicians

Number of Pages Required

2 page

Colors
ec1f27

Requirements
Must have
• - A Picture on the front page that promotes the main upcomming event
• - Attention for recruiting new musicians
• - Pictures with young musicians (white back ground, see examples)
• - Responsive
• - Please use the logo attached
Should not have
• The brown colors of the current website (kvb-veldhorst.example)

```html
<!DOCTYPE html>
<html lang="en">
<head>
<meta charset="utf-8">
<title>Veldhorst Jeugd Orkest</title>
<link href="https://fonts.googleapis.com/css2?family=Merienda:wght@400;700&family=Poppins:wght@400;500;600&display=swap" rel="stylesheet">
<style>
:root{
  --red:#ec1f27;
  --ink:#1d1d1d;
  --muted:#5a5a5a;
  --dark-box:#231a1b;
  --footer:#262626;
  --soft:#f7f7f7;
  --white:#ffffff;
}
*{margin:0;padding:0;box-sizing:border-box}
html,body{width:1200px;height:3597px;overflow:hidden;background:var(--white)}
body{position:relative;font-family:"Poppins",sans-serif;color:var(--ink)}
.abs{position:absolute}
.script{font-family:"Merienda",cursive;font-weight:700}
.btn{position:absolute;display:flex;align-items:center;justify-content:center;background:var(--red);color:var(--white);font-size:11px;font-weight:600;border-radius:6px;box-shadow:0 2px 6px rgba(0,0,0,.18)}
.topbar{font-size:11px;color:var(--ink);top:18px;display:flex;align-items:center;gap:6px}
.logo-badge{left:537px;top:-63px;width:126px;height:126px;border-radius:50%;background:var(--red);display:flex;align-items:flex-end;justify-content:center;padding-bottom:10px;color:var(--white);font-size:10px;font-weight:600;text-align:center;line-height:1.1}
.social{position:absolute;width:30px;height:30px;border-radius:50%;background:var(--ink);color:var(--white);font-size:7px;display:flex;align-items:center;justify-content:center}
.nav{top:80px;font-size:11.5px;color:var(--ink)}
.nav span{position:absolute;transform:translateX(-50%);white-space:nowrap}
.rule{left:0;top:109px;width:1200px;height:1px;background:#e6e6e6}
.hero{left:0;top:110px;width:1200px;height:490px;background:#050505;overflow:hidden}
.hero-photo{position:absolute;left:237px;top:0;width:727px;height:490px;background:radial-gradient(ellipse at 55% 35%,#a5735a 0%,#5b3324 40%,#1a0e0a 75%,#050505 100%)}
.hero-title{left:0;width:1200px;text-align:center;color:var(--white)}
.red{color:var(--red)}
.dot{position:absolute;top:376px;width:12px;height:12px;border-radius:50%;background:var(--white)}
.about-photo{left:111px;top:670px;width:392px;height:392px;border-radius:50%;background:radial-gradient(circle at 45% 45%,#b5562c,#6b2a14 60%,#2c130a);border-right:4px solid var(--red)}
.h2{font-size:54px;line-height:1;color:var(--ink)}
.copy{font-size:11.3px;line-height:18px;color:var(--muted)}
.events{left:94px;top:1131px;width:1012px;height:466px;background:var(--dark-box)}
.soft-band{left:0;top:1565px;width:1200px;height:500px;background:var(--soft)}
.recruit{position:absolute;top:1766px;width:182px;height:182px;border-radius:50%;border-top:5px solid var(--red)}
.foot-list{font-size:10.5px;color:var(--white);list-style:none}
.foot-list li{position:absolute;white-space:nowrap;padding-left:16px}
.foot-list li::before{content:"";position:absolute;left:0;top:6px;width:5px;height:5px;border-radius:50%;background:var(--white)}
.sep{position:absolute;top:3140px;width:1px;height:250px;background:linear-gradient(transparent,rgba(255,255,255,.15),transparent)}
.program p{margin-bottom:3px}
</style>
</head>
<body>

<div class="abs topbar" style="left:94px">
  <svg width="10" height="12" viewBox="0 0 10 12"><path d="M3 1 L1 2 Q0 6 4 11 L6 10 L5 8 L3.5 8.5 Q2 6 2.5 3.5 L4 3 Z" fill="#1d1d1d"/></svg>40 12 34 56
  <svg width="12" height="10" viewBox="0 0 12 10" style="margin-left:10px"><rect x="0.5" y="0.5" width="11" height="9" fill="none" stroke="#1d1d1d"/><path d="M0.5 0.5 L6 5 L11.5 0.5" fill="none" stroke="#1d1d1d"/></svg>info@kvb-veldhorst.example
</div>
<div class="abs logo-badge">Veldhorst<br>Jeugd Orkest</div>
<div class="social" style="left:890px;top:11px">Share</div>
<div class="social" style="left:929px;top:11px">Chat</div>
<div class="social" style="left:968px;top:11px">Video</div>
<div class="btn" style="left:1021px;top:11px;width:84px;height:31px;border-radius:4px">Log In</div>
<nav class="abs nav" style="left:0;width:1200px">
  <span style="left:210px">Home</span><span style="left:288px">Orchestra</span><span style="left:379px">Play along</span><span style="left:467px">Concerts</span><span style="left:542px">Tours</span><span style="left:614px">Partners</span><span style="left:712px">Friends Former</span><span style="left:815px">members</span><span style="left:940px">Contact &amp; organization</span>
</nav>
<div class="abs rule"></div>

<section class="abs hero">
  <div class="hero-photo" role="img" aria-label="Close-up of a young violinist playing during a concert"></div>
  <div class="abs hero-title script" style="top:122px;font-size:66px;line-height:1">one of the best <span class="red">classical</span></div>
  <div class="abs hero-title script" style="top:192px;font-size:40px;line-height:1"><span class="red">youth</span> orchestras in the county</div>
  <div class="btn" style="left:539px;top:270px;width:122px;height:28px">Contact Us</div>
  <div class="dot" style="left:574px"></div><div class="dot" style="left:593px;background:var(--red)"></div><div class="dot" style="left:613px"></div>
</section>
<svg class="abs" style="left:0;top:520px" width="1200" height="90" viewBox="0 0 1200 90">
  <path d="M0 78 Q600 -45 1200 78 L1200 90 L0 90 Z" fill="#fff"/>
  <path d="M0 70 Q600 -55 1200 70" fill="none" stroke="#ec1f27" stroke-width="5"/>
</svg>

<div class="abs about-photo" role="img" aria-label="Orchestra rehearsing, seen from above"></div>
<h2 class="abs h2 script" style="left:549px;top:714px">About Us</h2>
<p class="abs copy" style="left:549px;top:793px;width:535px">Are you planning to become a member of our orchestra? Then come along! At every VJO rehearsal you are cordially invited to listen &amp; watch with your own ears &amp; eyes and maybe even play along! Every Friday evening we play in the Sint-Jozefkerk on Kerkplein 12 in the heart of Veldhorst. It is a 15-minute walk from the Veldhorst CS.</p>
<p class="abs copy" style="left:549px;top:884px;width:535px">We rehearse from 7:00 pm to 10:00 pm with a break around 8:15 pm. Let us know when you plan to come via orkestzaken@kvb-veldhorst.example .</p>
<div class="btn" style="left:549px;top:939px;width:123px;height:36px">Read More</div>

<div class="abs soft-band"></div>
<div class="abs events"></div>
<svg class="abs" style="left:176px;top:1180px" width="342" height="372" viewBox="0 0 342 372">
  <rect x="0" y="0" width="341" height="371" fill="none" stroke="#6c6c6c" stroke-width="5"/>
  <path d="M2 100 L2 2 L100 2" fill="none" stroke="#ec1f27" stroke-width="6"/>
  <path d="M339 270 L339 369 L240 369" fill="none" stroke="#ec1f27" stroke-width="6"/>
</svg>
<div class="abs" role="img" aria-label="Video of the orchestra and choir performing in a church" style="left:186px;top:1190px;width:321px;height:351px;background:linear-gradient(180deg,#6a6458 0%,#7a3f9c 30%,#2b2233 60%,#0d0d10 100%)"></div>
<svg class="abs" style="left:322px;top:1338px" width="50" height="56" viewBox="0 0 50 56"><path d="M2 2 L48 28 L2 54 Z" fill="#fff"/></svg>
<h2 class="abs h2 script" style="left:563px;top:1258px;color:var(--white)">Upcoming Events</h2>
<p class="abs copy" style="left:568px;top:1341px;width:440px;color:#e9e9e9;font-size:11px">the last rehearsal of 2019! We're playing Favre with Thomas as a soloist. We wish you very pleasant days and a healthy and musical 2020. Please see you in the new year (that sounds far) at our new year's concert</p>
<div class="btn" style="left:568px;top:1410px;width:122px;height:37px">Read More</div>

<h2 class="abs h2 script" style="left:0;width:1200px;text-align:center;top:1660px;font-size:52px">Attention for recruiting new musicians</h2>
<div class="recruit" role="img" aria-label="Portrait of a young clarinettist" style="left:124px;background:linear-gradient(160deg,#3f5a3a,#253026)"></div>
<div class="recruit" role="img" aria-label="Young flute players rehearsing" style="left:381px;background:linear-gradient(160deg,#b3b0aa,#3a3434)"></div>
<div class="recruit" role="img" aria-label="Young violinist in concert" style="left:637px;background:linear-gradient(160deg,#5a4a3a,#1a1512)"></div>
<div class="recruit" role="img" aria-label="Young violinist portrait" style="left:894px;background:linear-gradient(160deg,#d6d6d6,#2a2a2a)"></div>
<div class="btn" style="left:539px;top:1999px;width:122px;height:38px">Read More</div>

<div class="abs" role="img" aria-label="Conductor leading a choir in a concert hall" style="left:0;top:2040px;width:1200px;height:475px;background:linear-gradient(180deg,#8a8378 0%,#4d4742 40%,#1c1a19 100%)"></div>
<svg class="abs" style="left:0;top:2035px" width="1200" height="80" viewBox="0 0 1200 80">
  <path d="M0 0 L1200 0 L1200 15 Q600 100 0 15 Z" fill="#f7f7f7"/>
  <path d="M0 15 Q600 100 1200 15" fill="none" stroke="#ec1f27" stroke-width="5"/>
</svg>
<svg class="abs" style="left:0;top:2470px" width="1200" height="50" viewBox="0 0 1200 50">
  <path d="M0 40 Q600 -10 1200 40 L1200 50 L0 50 Z" fill="#fff"/>
  <path d="M0 38 Q600 -12 1200 38" fill="none" stroke="#ec1f27" stroke-width="4"/>
</svg>
<div class="abs script" style="left:0;width:1200px;text-align:center;top:2200px;font-size:48px;line-height:1;color:var(--white)">REGISTER AS AN OLD MEMBER</div>
<div class="abs script" style="left:0;width:1200px;text-align:center;top:2252px;font-size:40px;line-height:1;color:var(--white)">Are you not yet registered in our system?</div>
<div class="btn" style="left:539px;top:2325px;width:122px;height:36px;font-size:16px">Join Us</div>

<h2 class="abs h2 script" style="left:94px;top:2614px">Program:</h2>
<div class="abs copy program" style="left:94px;top:2684px;width:510px;font-size:11px;line-height:18px">
  <p>- Hendrik Molenaar (1878-1950) - Harbour Lights Overture Op. 7 (1923)</p>
  <p>- Lucien Favre (1889-1961) - Concert Piece for horn &amp; orchestra, Op. 31 (1931) - Soloist: Thomas de Wit (from his own orchestra)</p>
  <p>I. Allegro moderato</p>
  <p>II. Adagio</p>
  <p>III. Allegro non troppo</p>
  <p>- Karel Novotny (1884-1955) - Three movements from: Symphony No. 2 in E minor, Op. 19 (1927)</p>
  <p>I. Allegro con brio</p>
  <p>II. Adagio</p>
</div>
<div class="btn" style="left:95px;top:2918px;width:121px;height:37px">Read More</div>
<div class="btn" style="left:222px;top:2918px;width:122px;height:37px">Buy Ticket</div>
<div class="abs" role="img" aria-label="Concert poster with colourful bubbles and a large orange speech shape" style="left:647px;top:2590px;width:459px;height:400px;background:linear-gradient(160deg,#e6d3ea 0%,#e6d3ea 45%,#f15a2a 75%,#e6d3ea 100%)"></div>

<div class="abs" style="left:0;top:3045px;width:1200px;height:552px;background:var(--footer)"></div>
<svg class="abs" style="left:0;top:3040px" width="1200" height="80" viewBox="0 0 1200 80">
  <path d="M0 0 L1200 0 L1200 6 Q600 110 0 6 Z" fill="#fff"/>
  <path d="M0 10 Q600 115 1200 10" fill="none" stroke="#ec1f27" stroke-width="5"/>
</svg>
<div class="abs" style="left:140px;top:3205px;width:200px;text-align:center;color:var(--white);font-size:26px;font-weight:500;line-height:1.15">Veldhorst<br>Jeugd Orkest</div>
<div class="social" style="left:186px;top:3326px;background:var(--white);color:var(--footer)">Share</div>
<div class="social" style="left:225px;top:3326px;background:var(--white);color:var(--footer)">Chat</div>
<div class="social" style="left:264px;top:3326px;background:var(--white);color:var(--footer)">Video</div>
<div class="sep" style="left:356px"></div><div class="sep" style="left:636px"></div><div class="sep" style="left:824px"></div>
<div class="abs script" style="left:398px;top:3188px;font-size:19px;font-weight:400;color:var(--white)">Sitemap</div>
<ul class="foot-list">
  <li style="left:399px;top:3230px">Home</li><li style="left:399px;top:3257px">Orchestra</li><li style="left:399px;top:3283px">Play along</li><li style="left:399px;top:3310px">Concerts</li><li style="left:399px;top:3337px">Tours</li>
  <li style="left:507px;top:3230px">Partners</li><li style="left:507px;top:3257px">FriendsFormer</li><li style="left:507px;top:3283px">members</li>
  <li style="left:680px;top:3230px">commissies</li><li style="left:680px;top:3257px">dirigent</li><li style="left:680px;top:3283px">gedragscode</li><li style="left:680px;top:3310px">orkestleden</li>
</ul>
<div class="abs script" style="left:866px;top:3188px;font-size:19px;font-weight:400;color:var(--white)">Contact Us</div>
<svg class="abs" style="left:866px;top:3232px" width="8" height="11" viewBox="0 0 8 11"><path d="M4 11 L1 5 A3 3 0 1 1 7 5 Z" fill="#fff"/><circle cx="4" cy="4" r="1.3" fill="#262626"/></svg>
<div class="abs" style="left:868px;top:3284px;width:5px;height:5px;border-radius:50%;background:#fff"></div>
<div class="abs" style="left:868px;top:3318px;width:5px;height:5px;border-radius:50%;background:#fff"></div>
<svg class="abs" style="left:866px;top:3349px" width="9" height="10" viewBox="0 0 10 12"><path d="M3 1 L1 2 Q0 6 4 11 L6 10 L5 8 L3.5 8.5 Q2 6 2.5 3.5 L4 3 Z" fill="#fff"/></svg>
<div class="abs" style="left:886px;top:3228px;width:220px;font-size:10.5px;line-height:18px;color:var(--white)">Veldhorst Jeugd Orkest,Postbus 456 1234AB Veldhorst</div>
<div class="abs" style="left:886px;top:3277px;font-size:10.5px;color:var(--white)">NL00 BANK 0123 4567 89</div>
<div class="abs" style="left:886px;top:3310px;width:220px;font-size:10.5px;line-height:18px;color:var(--white)">t.n.v. VJO Jeugd Symfonieorkest, prov. Veldland te Veldhorst</div>
<div class="abs" style="left:886px;top:3346px;font-size:10.5px;color:var(--white)">40 12 34 56</div>
<div class="abs" style="left:265px;top:3459px;width:741px;height:1px;background:rgba(255,255,255,.2)"></div>
<div class="abs" style="left:0;width:1200px;top:3490px;text-align:center;font-size:10px;color:#bdbdbd">©2020 <span style="font-size:15px;font-weight:500;color:var(--white)">Jeugd orkest</span> All rights reserved</div>

</body>
</html>
```